Elegant Black Candle Label Design!

I need a 2.375" tall by 3.0" wide candle label design. I'm looking for simple and elegant. Black label with silver leaf border and lettering. Label needs to have the following information on it: Fern Hollow Candle Co. as the company name, scent name in the middle and in smaller font, it needs to say Made in USA, All Natural, 8oz. Attached photos are for inspiration.

Target Market(s)

People looking for high end, all natural candle fragrances

Industry/Entity Type

Candle-Spa

Colors

Designer to choose only greyscale colors for use in the design.

Requirements
Must have
• Company Name, Scent (ability to change scent names), All Natural, Made in USA, 8oz
Nice to have
• Black background, silver leaf border and silver leaf font. Elegant fonts maybe slightly cursive

```html
<!DOCTYPE html>
<html lang="en">
<head>
<meta charset="utf-8">
<title>Fern Hollow Candle Co. — Label</title>
<link rel="stylesheet" href="https://fonts.googleapis.com/css2?family=Josefin+Sans:wght@500;600&family=Montserrat:wght@500;600&family=Cormorant+Garamond:ital,wght@1,500&display=swap">
<style>
  :root {
    --page: #ecedee;
    --label-black: #0d0d0d;
    --silver-light: #f2f2f2;
    --silver-mid: #bcbcbc;
    --silver-dark: #8a8a8a;
    --panel-white: #f7f7f7;
    --ink: #141414;
    --rule: #9a9a9a;
  }
  html, body {
    margin: 0;
    width: 1200px;
    height: 1200px;
    overflow: hidden;
    background: var(--page);
  }
  .canvas {
    position: relative;
    width: 1200px;
    height: 1200px;
  }
  .label {
    position: absolute;
    left: 0;
    top: 0;
  }
  .brand-name {
    font-family: "Josefin Sans", sans-serif;
    font-weight: 500;
    fill: var(--ink);
    letter-spacing: 2px;
  }
  .scent-name {
    font-family: "Cormorant Garamond", serif;
    font-style: italic;
    font-weight: 500;
    fill: var(--ink);
    letter-spacing: 1px;
  }
  .details {
    font-family: "Montserrat", sans-serif;
    fill: var(--ink);
  }
  .details--strong { font-weight: 600; }
  .details--plain { font-weight: 500; }
</style>
</head>
<body>
<div class="canvas">
  <svg class="label" width="1200" height="1200" viewBox="0 0 1200 1200" xmlns="http://www.w3.org/2000/svg">
    <defs>
      <linearGradient id="silverLeaf" x1="0" y1="0" x2="1" y2="1">
        <stop offset="0" stop-color="var(--silver-dark)"/>
        <stop offset="0.2" stop-color="var(--silver-light)"/>
        <stop offset="0.4" stop-color="var(--silver-mid)"/>
        <stop offset="0.55" stop-color="var(--silver-light)"/>
        <stop offset="0.75" stop-color="var(--silver-dark)"/>
        <stop offset="1" stop-color="var(--silver-light)"/>
      </linearGradient>
    </defs>

    <!-- silver leaf border: 3in wide x 2.375in tall -->
    <rect class="label-border" x="80" y="188" width="1040" height="823" fill="url(#silverLeaf)"/>

    <!-- black field -->
    <rect class="label-field" x="92" y="231" width="1016" height="760" fill="var(--label-black)"/>

    <!-- double frame lines -->
    <rect class="frame-outer" x="102" y="241" width="996" height="740" fill="none" stroke="var(--silver-light)" stroke-width="3"/>
    <rect class="frame-inner" x="112" y="251" width="976" height="720" fill="none" stroke="var(--silver-light)" stroke-width="1.5"/>

    <!-- corner flourishes -->
    <g fill="var(--silver-mid)">
      <rect role="img" aria-label="corner flourish" x="118" y="257" width="24" height="24"/>
      <rect role="img" aria-label="corner flourish" x="1058" y="257" width="24" height="24"/>
      <rect role="img" aria-label="corner flourish" x="118" y="941" width="24" height="24"/>
      <rect role="img" aria-label="corner flourish" x="1058" y="941" width="24" height="24"/>
    </g>

    <!-- white hexagon panel -->
    <polygon class="name-panel" points="420,254 780,254 930,382 930,842 780,968 420,968 270,842 270,382"
             fill="var(--panel-white)" stroke="var(--silver-mid)" stroke-width="4"/>
    <polygon points="426,266 774,266 918,388 918,836 774,956 426,956 282,836 282,388"
             fill="none" stroke="var(--rule)" stroke-width="1.5"/>

    <!-- flower emblem area -->
    <circle role="img" aria-label="flower emblem" cx="600" cy="320" r="42" fill="#cfcfcf"/>

    <!-- company name -->
    <text class="brand-name" x="600" y="458" font-size="64" text-anchor="middle">FERN HOLLOW</text>
    <text class="brand-name" x="600" y="546" font-size="64" text-anchor="middle">CANDLE CO.</text>

    <!-- scent name (changeable) -->
    <text class="scent-name" x="600" y="620" font-size="46" text-anchor="middle">Cedar &amp; Sage</text>

    <!-- divider -->
    <line x1="340" y1="676" x2="562" y2="676" stroke="var(--rule)" stroke-width="2"/>
    <line x1="638" y1="676" x2="860" y2="676" stroke="var(--rule)" stroke-width="2"/>
    <rect role="img" aria-label="small sprig ornament" x="574" y="669" width="52" height="14" rx="7" fill="var(--ink)"/>

    <!-- details -->
    <text class="details details--strong" x="600" y="752" font-size="38" text-anchor="middle">MADE IN USA</text>
    <text class="details details--plain" x="600" y="820" font-size="33" text-anchor="middle">ALL NATURAL</text>
    <text class="details details--strong" x="600" y="888" font-size="35" text-anchor="middle">8OZ.</text>
  </svg>
</div>
</body>
</html>
```